Online Rug Store needs Clearance Banner

Website is: Lanternfield Carpets and Home
You can access it at: www.lanternfieldcarpetsandhome.com and login (top right) with password: trazok

*** update: When creating banners for my site, you have permission to use images from www.velbora.com, but ONLY for this project. The images/artwork are copyright allowable for use on www.lanternfieldcarpetsandhome.com projects.***

We need a home page banner sized 1000 wide x 500 tall pixels to promote a "Clearance Sale" on rugs. The banner can state:

1. Clearance Sale
2. Now in progress
3. Save an extra 20% with coupon code 'Mint20'
4. Ends March 31st
5. Plus Free Shipping and 30 day returns.

We prefer a banner that appears hand-drawn and artistic, not commercially produced. It is OK to use a room scene image, rug images, or just a colored/textured background with text and no images. Your choice.

Flat graphics with no shadows and 3-D effect preferred.
Attached is are 3 logo options, as well as an example banner with handcrafted, artistic styling that we prefer.

Target Market(s)

This should be an eye-catching banner to showcase a very urgent promotion. Consider using colors of red, white, gold, and black to make a strong statement on the home page.

Industry/Entity Type

Home And Garden

Requirements
Must have
• Winner must provide Photoshop editable file format (.psd format) including layers that can be edited.
Nice to have
• Hand-drawn, stenciled, scribbled, artistic graphics and fonts is nice because we sell rugs that are made by hand.
Should not have
• little to no shadowing. Avoid computerized graphics.

```html
<!DOCTYPE html>
<html lang="en">
<head>
<meta charset="utf-8">
<title>Clearance Sale on Rugs – Lanternfield Carpets and Home</title>
<link rel="stylesheet" href="https://fonts.googleapis.com/css2?family=Jost:wght@300;400&display=swap">
<style>
  :root {
    --floor-light: #8a8784;
    --floor-mid: #6a6865;
    --floor-dark: #3e3d3c;
    --rug-red: #c8283a;
    --rug-pink: #d8407e;
    --rug-teal: #3aa6a8;
    --rug-gold: #c9b23a;
    --rug-wine: #7a1e34;
    --text-white: #ffffff;
  }
  html, body {
    margin: 0;
    padding: 0;
    overflow: hidden;
    background: var(--floor-mid);
  }
  .banner {
    position: relative;
    width: 1200px;
    height: 600px;
    overflow: hidden;
    font-family: "Jost", sans-serif;
    color: var(--text-white);
  }
  .banner__scene {
    position: absolute;
    inset: 0;
    width: 1200px;
    height: 600px;
  }
  .banner__copy {
    position: absolute;
    inset: 0;
    font-weight: 300;
    text-transform: uppercase;
    line-height: 1;
  }
  .banner__copy p,
  .banner__copy h1 {
    position: absolute;
    left: 34px;
    margin: 0;
    white-space: nowrap;
  }
  .offer-details {
    top: 168px;
    font-size: 24px;
    font-weight: 400;
    letter-spacing: 1px;
    line-height: 1.3;
  }
  .sale-status {
    top: 262px;
    font-size: 68px;
    letter-spacing: 1px;
  }
  .site-name {
    top: 336px;
    font-size: 48px;
    letter-spacing: 0.5px;
  }
  .sale-headline {
    top: 418px;
    width: 770px;
    font-weight: 300;
    font-size: 97px;
    letter-spacing: 1px;
    line-height: 0.8;
  }
  .sale-headline__line {
    display: block;
  }
  .sale-headline__line--right {
    text-align: right;
  }
</style>
</head>
<body>
  <main class="banner">
    <svg class="banner__scene" viewBox="0 0 1200 600" role="img"
         aria-label="Photo of a colourful handmade patchwork rug in red, pink, teal and gold lying on a grey concrete floor">
      <defs>
        <linearGradient id="floorTone" x1="0" y1="0" x2="1" y2="1">
          <stop offset="0" stop-color="var(--floor-light)"/>
          <stop offset="0.55" stop-color="var(--floor-mid)"/>
          <stop offset="1" stop-color="var(--floor-dark)"/>
        </linearGradient>
        <linearGradient id="rugTone" x1="0" y1="0" x2="1" y2="1">
          <stop offset="0" stop-color="var(--rug-pink)"/>
          <stop offset="0.3" stop-color="var(--rug-red)"/>
          <stop offset="0.5" stop-color="var(--rug-teal)"/>
          <stop offset="0.68" stop-color="var(--rug-gold)"/>
          <stop offset="0.85" stop-color="var(--rug-wine)"/>
          <stop offset="1" stop-color="var(--rug-pink)"/>
        </linearGradient>
      </defs>
      <rect class="floor" width="1200" height="600" fill="url(#floorTone)"/>
      <polygon class="rug" points="624,0 1158,22 1134,600 156,600 204,312" fill="url(#rugTone)"/>
    </svg>

    <div class="banner__copy">
      <p class="offer-details">Save an extra 20% with code Mint20 · Ends March 31st<br>Plus free shipping and 30 day returns</p>
      <p class="sale-status">Now in progress</p>
      <p class="site-name">Lanternfield Carpets and Home</p>
      <h1 class="sale-headline">
        <span class="sale-headline__line">Clearance Sale</span>
        <span class="sale-headline__line sale-headline__line--right">On Rugs</span>
      </h1>
    </div>
  </main>
</body>
</html>
```